Business Card Design - Lumo Fitters

Lumo Fitters is a service company which carried out installation and maintenance work in the GPS Tracking industry.

We install and maintain GPS Tracking hardware into cars, trucks etc.

We have an existing design with existing logo which I would like to improve on. I would like to be able to edit the design in the future when we have new staff come on board. We currently have 8 or so different employees who would all require cards - ideally I need to be able to edit a template in photoshop or something.

The back of the existing design has a white outline of Australia with a white dot over: Brisbane, Sydney, Melbourne, Adelaide and Perth.

Our current cards are mainly black, our uniforms are black - happy to look at changing that if the look is right.

We strive to be organised, professional and we are working in the technology sector.

Cheers.

Industry/Entity Type

Business

Contact Information for Business Card

Name
Mobile number
Email address
Web address

Requirements
Must have
• Map of Australia as mentioned above.

```html
<!DOCTYPE html>
<html lang="en">
<head>
<meta charset="utf-8">
<title>Lumo Fitters – Business Card</title>
<link rel="stylesheet" href="https://fonts.googleapis.com/css2?family=Questrial&display=swap">
<style>
  :root {
    --stage: #2a2a2c;
    --card: #0b0b0c;
    --ink: #f4f4f4;
    --ink-soft: #d8d8d8;
    --accent: #3f7fc4;
    --map-light: #3a3a3d;
    --map-dark: #1a1a1c;
  }
  * { margin: 0; padding: 0; box-sizing: border-box; }
  html, body { width: 1200px; height: 871px; overflow: hidden; }
  body {
    background: var(--stage);
    font-family: "Questrial", "Century Gothic", sans-serif;
    color: var(--ink);
    display: flex;
    align-items: center;
    justify-content: center;
    gap: 40px;
  }
  .card {
    position: relative;
    width: 550px;
    height: 336px;
    background: var(--card);
    overflow: hidden;
  }
  .wordmark {
    position: absolute;
    font-size: 44px;
    font-weight: 400;
    letter-spacing: -0.5px;
    color: var(--ink);
    white-space: nowrap;
  }
  .card--front .wordmark { left: 150px; top: 62px; }
  .card--back .wordmark { left: 36px; top: 252px; color: var(--ink-soft); }
  .holder-name {
    position: absolute;
    left: 42px;
    top: 146px;
    font-size: 17px;
    letter-spacing: 1.5px;
  }
  .contact-list {
    position: absolute;
    left: 296px;
    top: 176px;
    list-style: none;
  }
  .contact-list li {
    display: flex;
    align-items: center;
    gap: 16px;
    height: 22px;
    font-size: 13px;
    letter-spacing: 1.4px;
    color: var(--ink);
  }
  .contact-list svg { width: 15px; height: 15px; flex: none; }
  .stripes { position: absolute; left: 0; top: 0; }
  .australia-map {
    position: absolute;
    left: 270px;
    top: 24px;
    width: 240px;
    height: 210px;
    border-radius: 40px 60px 50px 70px;
    background: radial-gradient(circle at 55% 45%, var(--map-light), var(--map-dark) 75%);
  }
</style>
</head>
<body>

  <section class="card card--back">
    <div class="australia-map" role="img" aria-label="Outline map of Australia with state borders and dots over Brisbane, Sydney, Melbourne, Adelaide and Perth"></div>
    <div class="wordmark">Lumo Fitters</div>
  </section>

  <section class="card card--front">
    <div class="wordmark">Lumo Fitters</div>
    <p class="holder-name">Dean Harwell</p>

    <ul class="contact-list">
      <li>
        <svg viewBox="0 0 16 16" fill="none" stroke="var(--accent)" stroke-width="1.4"><path d="M2 6c0-2 3-3 6-3s6 1 6 3l-2 1-1-2H5L4 7z"/><rect x="4" y="8" width="8" height="5" rx="1"/></svg>
        0400 182 644
      </li>
      <li>
        <svg viewBox="0 0 16 16" fill="none" stroke="var(--accent)" stroke-width="1.4"><rect x="4" y="1.5" width="8" height="4"/><rect x="1.5" y="5.5" width="13" height="6" rx="1"/><rect x="4" y="10" width="8" height="4.5"/></svg>
        (07) 3000 4821
      </li>
      <li>
        <svg viewBox="0 0 16 16" fill="none" stroke="var(--accent)" stroke-width="1.4"><rect x="1.5" y="3.5" width="13" height="9"/><path d="M1.5 3.5 8 9l6.5-5.5"/></svg>
        dean@lumofitters.com.au
      </li>
      <li>
        <svg viewBox="0 0 16 16" fill="none" stroke="var(--accent)" stroke-width="1.3"><circle cx="8" cy="8" r="6.2"/><ellipse cx="8" cy="8" rx="2.8" ry="6.2"/><path d="M1.8 8h12.4"/></svg>
        www.lumofitters.com.au
      </li>
    </ul>

    <svg class="stripes" width="550" height="336" viewBox="0 0 550 336">
      <defs>
        <linearGradient id="whiteBand" x1="0" x2="1" y1="0" y2="0">
          <stop offset="0" stop-color="#ffffff"/>
          <stop offset="1" stop-color="#cfcfcf"/>
        </linearGradient>
      </defs>
      <polygon points="0,292 226,292 244,314 0,314" fill="url(#whiteBand)"/>
      <polygon points="248,316 550,316 550,332 262,332" fill="var(--accent)"/>
    </svg>
  </section>

</body>
</html>
```